Packaging & Label Design for CDB Products

We are a European CBD company specialising in athletic recovery, sleep improvement and wellness.

We would like the packaging to incorporate our logo and name (and font 'Codec') 'Meridell CBD'. The design must be transferable to all of our products. CBD Oils, Balms, Lip Balm and Vape E-Liquid.

We would like it to be simple but eye-catching and modern. We don't want bright colours. Preferred pallet of muted greys, blacks, white and pastel colours. Geometric concepts, possibly using different colours for each item of the range, we are open to new and fresh ideas (we are seeking you for your experience) and when we find the right design we would likely throw more work in your direction..

Our product range is not complete so the designer must be flexible with some changes and provide files where format can be easily edited by packaging manufacturer. We are also waiting for dimensions for the labels and boxes for several products and will supply the designer with full dimensions of all products once selected.

Oil Box: 2.6 x 9.0 x 2.6 cm (open format 16.7 x 11.6cm)
Labels: 7.8 x 3.3 cm (Front and Back)

Our expected product range will be:
CBD Oil 1000mg
CBD Oil 3000mg
CBD Balm 100mg
CBD Balm 300mg
E-Liquid 500mg
Lip Balm 50mg

We look forward to seeing your ideas.

Best Regards
Meridell CBD

```html
<!DOCTYPE html>
<html lang="en">
<head>
<meta charset="utf-8">
<title>Meridell CBD Oil Labels</title>
<link rel="stylesheet" href="https://fonts.googleapis.com/css2?family=Montserrat:wght@500;600;700&display=swap">
<style>
  :root {
    --canvas: #ffffff;
    --ink-black: #141414;
    --shade-dark: #3a3a3a;
    --shade-mid: #6e6e6e;
    --shade-light: #8a8a8a;
    --type-white: #f4f4f4;
  }
  * { box-sizing: border-box; margin: 0; padding: 0; }
  html, body {
    width: 1200px; height: 1200px; overflow: hidden;
    background: var(--canvas);
    font-family: "Montserrat", Arial, sans-serif;
  }
  .range {
    position: absolute; left: 125px; top: 350px;
    display: flex; gap: 40px;
  }
  .label {
    position: relative; width: 290px; height: 500px;
    color: var(--type-white); overflow: hidden;
  }
  .label-field { position: absolute; inset: 0; width: 100%; height: 100%; }
  .label .field-dark { fill: var(--ink-black); }
  .label .field-tone { fill: var(--shade-dark); }
  .label--strong .field-tone { fill: var(--shade-mid); }
  .label--strong .field-dark { fill: #262626; }
  .brand {
    position: absolute; left: 30px; top: 40px;
    font-weight: 700; font-size: 27px; letter-spacing: 2.5px;
  }
  .product {
    position: absolute; left: 32px; top: 82px;
    font-weight: 600; font-size: 18px; letter-spacing: 1.5px;
  }
  .mark {
    position: absolute; left: 0; right: 0; top: 175px;
    display: flex; flex-direction: column; align-items: center; gap: 12px;
  }
  .mark-dot {
    width: 74px; height: 74px; border-radius: 50%;
    background: var(--type-white);
  }
  .mark-name {
    font-weight: 600; font-size: 13px; letter-spacing: 2px;
  }
  .strength {
    position: absolute; right: 14px; top: 205px;
    writing-mode: vertical-rl; transform: rotate(180deg);
    font-weight: 500; font-size: 25px; letter-spacing: 1px;
  }
  .strength small { font-size: 13px; }
  .volume {
    position: absolute; left: 14px; top: 215px;
    writing-mode: vertical-rl; transform: rotate(180deg);
    font-weight: 500; font-size: 10px; line-height: 1.3; letter-spacing: 1px;
    text-align: center;
  }
  .extract {
    position: absolute; left: 82px; top: 412px;
    font-weight: 600; font-size: 14px; line-height: 26px; letter-spacing: 1.6px;
  }
</style>
</head>
<body>
  <main class="range">
    <section class="label">
      <svg class="label-field" viewBox="0 0 290 500" preserveAspectRatio="none" aria-hidden="true">
        <rect class="field-tone" width="290" height="500"/>
        <polygon class="field-dark" points="0,0 290,0 290,40 0,480"/>
      </svg>
      <div class="brand">MERIDELL</div>
      <div class="product">CBD OIL</div>
      <div class="mark"><span class="mark-dot"></span><span class="mark-name">MERIDELL CBD</span></div>
      <div class="volume">1.02 FL OZ<br>( 30 ML)</div>
      <div class="strength">1000 <small>mg</small></div>
      <div class="extract">FULL SPECTRUM<br>HEMP EXTRACTS</div>
    </section>

    <section class="label label--strong">
      <svg class="label-field" viewBox="0 0 290 500" preserveAspectRatio="none" aria-hidden="true">
        <rect class="field-tone" width="290" height="500"/>
        <polygon class="field-dark" points="0,0 290,0 290,40 0,480"/>
      </svg>
      <div class="brand">MERIDELL</div>
      <div class="product">CBD OIL</div>
      <div class="mark"><span class="mark-dot"></span><span class="mark-name">MERIDELL CBD</span></div>
      <div class="volume">1.02 FL OZ<br>( 30 ML)</div>
      <div class="strength">3000 <small>mg</small></div>
      <div class="extract">FULL SPECTRUM<br>HEMP EXTRACTS</div>
    </section>

    <section class="label">
      <svg class="label-field" viewBox="0 0 290 500" preserveAspectRatio="none" aria-hidden="true">
        <rect class="field-tone" width="290" height="500"/>
        <polygon class="field-dark" points="0,0 290,0 290,40 0,480"/>
      </svg>
      <div class="brand">MERIDELL</div>
      <div class="product">CBD OIL</div>
      <div class="mark"><span class="mark-dot"></span><span class="mark-name">MERIDELL CBD</span></div>
      <div class="volume">1.02 FL OZ<br>( 30 ML)</div>
      <div class="strength">1000 <small>mg</small></div>
      <div class="extract">FULL SPECTRUM<br>HEMP EXTRACTS</div>
    </section>
  </main>
</body>
</html>
```